Bookkeeping business needs a digital and print flyer

We need a flyer to promote our virtual bookkeeping services to small and mid-sized businesses in the United States. We want the content and design of the flyer to be consistent with our website: www.brightledgerbookkeeping.example. We would like both a print version and a digital version of the flyer.

```html
<!DOCTYPE html>
<html lang="en">
<head>
<meta charset="utf-8">
<title>Bright Ledger Bookkeeping – Flyer</title>
<link rel="stylesheet" href="https://fonts.googleapis.com/css2?family=Poppins:wght@300;400;500;600;700;800&display=swap">
<style>
  :root{
    --backdrop:#9e9e9e;
    --ink:#1f1f1f;
    --dark:#222222;
    --white:#ffffff;
    --yellow:#fbc531;
    --yellow-soft:#fde6a3;
    --yellow-pale:#fff3cf;
  }
  *{margin:0;padding:0;box-sizing:border-box}
  html,body{width:1200px;height:1200px;overflow:hidden}
  body{background:var(--backdrop);font-family:'Poppins',sans-serif;color:var(--ink);position:relative}
  .flyer{position:absolute;left:212px;top:112px;width:737px;height:954px;background:var(--white);overflow:hidden}
  .hero{position:absolute;left:0;top:0;width:737px;height:397px;
    background:radial-gradient(ellipse at 60% 45%,#3a3a3a 0%,#262626 55%,#1c1c1c 100%)}
  .brand{position:absolute;top:44px;left:0;width:100%;display:flex;justify-content:center;align-items:center;gap:12px}
  .brand-name{font-weight:300;font-size:22px;letter-spacing:1.5px;color:var(--white)}
  .brand-dot{width:34px;height:34px;border:2px solid var(--white);border-radius:50%}
  .headline{position:absolute;top:116px;width:100%;text-align:center;font-weight:700;font-size:45px;line-height:54px;color:var(--white)}
  .headline .accent{color:var(--yellow)}
  .tagline{position:absolute;top:235px;width:100%;text-align:center;font-size:16px;color:var(--white)}
  .dots{position:absolute;top:270px;left:0;width:100%;display:flex;justify-content:center;gap:7px}
  .dots span{width:17px;height:17px;border-radius:50%;border:1.5px solid #cfcfcf}
  .dots span.on{border-color:var(--yellow)}
  .meet{position:absolute;left:55px;top:321px;width:648px;height:135px;background:var(--yellow)}
  .meet-photo{position:absolute;left:0;top:0;width:128px;height:135px;background:linear-gradient(160deg,#e9b940,#6c6a72 60%,#2d3145)}
  .meet-title{position:absolute;left:141px;top:14px;font-size:30px;font-weight:400;line-height:34px}
  .meet-title b{font-weight:700}
  .meet-text{position:absolute;left:141px;top:54px;width:490px;font-size:12.6px;line-height:14.8px}
  .services{position:absolute;left:60px;top:478px;width:312px}
  .services-title{display:flex;align-items:flex-end;gap:5px;font-size:30px;line-height:34px;font-weight:400}
  .services-title::after{content:"";flex:1;height:1.5px;background:var(--ink);margin-bottom:8px}
  .services-sub{margin-top:2px;font-size:17.6px;line-height:22px;font-weight:600;color:var(--yellow)}
  .services-lead{margin-top:7px;font-size:13.4px;font-weight:500;white-space:nowrap}
  .benefits{position:absolute;left:55px;top:593px;width:320px}
  .benefits::before{content:"";position:absolute;left:20px;top:20px;width:1.5px;height:148px;background:var(--yellow)}
  .benefit{position:relative;height:49px;padding-left:52px;padding-right:10px;font-size:12.4px;line-height:13.8px}
  .benefit-icon{position:absolute;left:0;top:0;width:41px;height:41px;border-radius:50%;background:var(--yellow)}
  .benefit b{font-weight:700}
  .needs{position:absolute;left:408px;top:480px;width:312px}
  .needs-title{font-size:22px;line-height:26px;font-weight:700}
  .needs-sub{margin-top:7px;font-size:18px;font-weight:600;color:var(--yellow)}
  .needs-list{list-style:none;margin-top:4px}
  .needs-list li{position:relative;padding-left:16px;font-size:12px;line-height:13.8px;margin-bottom:3.9px}
  .needs-list svg{position:absolute;left:0;top:2px}
  .wave{position:absolute;left:0;top:790px}
  .footer{position:absolute;left:0;top:820px;width:737px;height:134px;background:var(--yellow)}
  .contact{position:absolute;top:57px;display:flex;align-items:center;gap:8px}
  .contact-icon{width:48px;height:48px;border-radius:50%;background:var(--dark);outline:1.5px solid var(--dark);outline-offset:2px;display:flex;align-items:center;justify-content:center;flex:none}
  .contact-label{font-size:17px;font-weight:700;line-height:19px}
  .contact-value{font-size:14.4px;line-height:17px;white-space:nowrap}
</style>
</head>
<body>
<div class="flyer">
  <header class="hero" role="img" aria-label="Dark photo of a desk with laptop, phone and plant">
    <div class="brand"><span class="brand-name">BRIGHT LEDGER BOOKKEEPING</span><span class="brand-dot"></span></div>
    <h1 class="headline">Virtual Bookkeeping for<br><span class="accent">Small Business</span></h1>
    <p class="tagline">Build Your Business by Focusing on What You Love</p>
    <div class="dots"><span></span><span class="on"></span><span></span></div>
  </header>

  <section class="meet">
    <div class="meet-photo" role="img" aria-label="Portrait photo of Marisa"></div>
    <h2 class="meet-title">Meet <b>Marisa</b></h2>
    <p class="meet-text">Hey there! I might be a bookkeeping nerd, but I still love to have some fun! You can catch me hanging out with my family, playing and teaching music, or cruising on my Ridgeway Trail bike. I’m also a pro at trip planning and love to hit up the mountains, lakes, and beaches for some R &amp; R time.</p>
  </section>

  <section class="services">
    <h2 class="services-title">Services</h2>
    <p class="services-sub">Say Hello to a reliable, hassle-free bookkeeping solution!</p>
    <p class="services-lead">What you get with Bright Ledger Bookkeeping</p>
  </section>

  <div class="benefits">
    <div class="benefit"><span class="benefit-icon"></span>Worry no more about finding time and energy to tackle bookkeeping<br><b>Hakuna Matata!</b></div>
    <div class="benefit"><span class="benefit-icon"></span>Keep more of your hard-earned money by maximizing tax deductions<br><b>Ka-Ching!</b></div>
    <div class="benefit"><span class="benefit-icon"></span>Understand those confusing financial reports to take your business to the next level <b>Booyah!</b></div>
    <div class="benefit"><span class="benefit-icon"></span>Celebrate each month’s wins during monthly consultations <b>Hooray!</b><br>Stress-free tax time <b>Oh Yeah!</b></div>
  </div>

  <section class="needs">
    <h2 class="needs-title">Bookkeeping Tailored to YOUR Business Needs</h2>
    <p class="needs-sub">Services Available:</p>
    <ul class="needs-list">
      <li><svg width="11" height="11" viewBox="0 0 12 12"><circle cx="6" cy="6" r="6" fill="#1f1f1f"/><path d="M3.2 6.2l1.9 1.9 3.8-3.9" stroke="#fff" stroke-width="1.6" fill="none"/></svg>Catch-up and clean-up services</li>
      <li><svg width="11" height="11" viewBox="0 0 12 12"><circle cx="6" cy="6" r="6" fill="#1f1f1f"/><path d="M3.2 6.2l1.9 1.9 3.8-3.9" stroke="#fff" stroke-width="1.6" fill="none"/></svg>Transaction importation and categorization</li>
      <li><svg width="11" height="11" viewBox="0 0 12 12"><circle cx="6" cy="6" r="6" fill="#1f1f1f"/><path d="M3.2 6.2l1.9 1.9 3.8-3.9" stroke="#fff" stroke-width="1.6" fill="none"/></svg>Monthly reconciliation of all accounts, including assets and loans.</li>
      <li><svg width="11" height="11" viewBox="0 0 12 12"><circle cx="6" cy="6" r="6" fill="#1f1f1f"/><path d="M3.2 6.2l1.9 1.9 3.8-3.9" stroke="#fff" stroke-width="1.6" fill="none"/></svg>Monthly financial reports (Balance Sheet, Income Statement, Cash Flow)</li>
      <li><svg width="11" height="11" viewBox="0 0 12 12"><circle cx="6" cy="6" r="6" fill="#1f1f1f"/><path d="M3.2 6.2l1.9 1.9 3.8-3.9" stroke="#fff" stroke-width="1.6" fill="none"/></svg>Monthly video conference</li>
      <li><svg width="11" height="11" viewBox="0 0 12 12"><circle cx="6" cy="6" r="6" fill="#1f1f1f"/><path d="M3.2 6.2l1.9 1.9 3.8-3.9" stroke="#fff" stroke-width="1.6" fill="none"/></svg>Annual tax-prep package sent to your preparer</li>
      <li><svg width="11" height="11" viewBox="0 0 12 12"><circle cx="6" cy="6" r="6" fill="#1f1f1f"/><path d="M3.2 6.2l1.9 1.9 3.8-3.9" stroke="#fff" stroke-width="1.6" fill="none"/></svg>A/R &amp; A/P</li>
      <li><svg width="11" height="11" viewBox="0 0 12 12"><circle cx="6" cy="6" r="6" fill="#1f1f1f"/><path d="M3.2 6.2l1.9 1.9 3.8-3.9" stroke="#fff" stroke-width="1.6" fill="none"/></svg>Payroll coordination</li>
      <li><svg width="11" height="11" viewBox="0 0 12 12"><circle cx="6" cy="6" r="6" fill="#1f1f1f"/><path d="M3.2 6.2l1.9 1.9 3.8-3.9" stroke="#fff" stroke-width="1.6" fill="none"/></svg>1099s</li>
      <li><svg width="11" height="11" viewBox="0 0 12 12"><circle cx="6" cy="6" r="6" fill="#1f1f1f"/><path d="M3.2 6.2l1.9 1.9 3.8-3.9" stroke="#fff" stroke-width="1.6" fill="none"/></svg>Bill pay and receipt management</li>
      <li><svg width="11" height="11" viewBox="0 0 12 12"><circle cx="6" cy="6" r="6" fill="#1f1f1f"/><path d="M3.2 6.2l1.9 1.9 3.8-3.9" stroke="#fff" stroke-width="1.6" fill="none"/></svg>Budgeting</li>
    </ul>
  </section>

  <svg class="wave" width="737" height="40" viewBox="0 0 737 40" preserveAspectRatio="none">
    <path d="M0 12 C120 30 230 4 370 14 S600 26 737 0 V40 H0Z" fill="var(--yellow-pale)"/>
    <path d="M0 20 C140 36 260 10 390 20 S610 30 737 10 V40 H0Z" fill="var(--yellow-soft)"/>
    <path d="M0 28 C150 40 280 20 400 28 S620 36 737 22 V40 H0Z" fill="var(--yellow)"/>
  </svg>

  <footer class="footer">
    <div class="contact" style="left:36px">
      <span class="contact-icon"><svg width="24" height="24" viewBox="0 0 24 24"><path d="M6.6 2.5l3 3.6-1.9 2.2c1.2 2.7 3.3 4.8 6 6l2.2-1.9 3.6 3-1.8 3.6C10.9 19.8 4.2 13.1 3 4.3z" fill="none" stroke="#fff" stroke-width="1.6" stroke-linejoin="round"/></svg></span>
      <div><div class="contact-label">Phone</div><div class="contact-value">555-014-2267</div></div>
    </div>
    <div class="contact" style="left:206px">
      <span class="contact-icon"><svg width="26" height="20" viewBox="0 0 26 20"><rect x="1" y="1" width="24" height="18" fill="none" stroke="#fff" stroke-width="1.5"/><path d="M1 1l12 10 12-10M1 19l9-8M25 19l-9-8" fill="none" stroke="#fff" stroke-width="1.5"/></svg></span>
      <div><div class="contact-label">Email</div><div class="contact-value">marisa@brightledger.example</div></div>
    </div>
    <div class="contact" style="left:520px">
      <span class="contact-icon"><svg width="20" height="26" viewBox="0 0 20 26"><path d="M10 25C4 17 1.5 12.5 1.5 9a8.5 8.5 0 0117 0c0 3.5-2.5 8-8.5 16z" fill="#fff"/><circle cx="10" cy="9" r="3.5" fill="#222"/></svg></span>
      <div><div class="contact-label">Location</div><div class="contact-value">Maple Ridge, NE</div></div>
    </div>
  </footer>
</div>
</body>
</html>
```